Redesign Canvas Art E-Commerce Website

Help! I hired a couple of companies on Tasklyn.com to build and design an e-commerce website for me. After three long and painful months, I have one that I believe is functional on the back-end, but aesthetically on the front end is a mess.

We are a small family business that will take your digital photo and manipulate it into a digitally created oil, watercolor or impressionist style pieces of artwork that we print on museum quality, gallery grade canvas and ship to the customer, ready to hang.

We are looking to create an e-commerce website where a customer can choose their art style, upload a photo, choose their canvas size and orientation (horizontal or vertical) and checkout. Within 48 hours, we will send them back a proof of their newly created, customized artwork for them to approve or not approve. If they approve, we print, package and ship them the product. If they do not approve, we offer unlimited revisions until they are happy.

As I mentioned, the back end functionality is already there, just need design help. No coding required

Here is a link to the development page that they created: https://brushvellomart.com/development/

As you can see, it looks off...doesnt line up properly, wasted space, weird font. Feel free to either correct the homepage they created or design an entirely new page. I am attaching some examples of before and after photos of artwork for reference. I also think the testimonials page and shop page can use a little style. The content is there and accurate, it just doesn't look pretty. Please keep in mind that our customers will probably not be very tech savvy. The customers will probably be sending us pics of kids, grandkids, pets, family portraits, vacation photos, etc.

Here is one of our competitors - www.pelfandquill.com
Their website looks clean and inviting.

Thank you in advance! Im looking forward to seeing the results. I am including our logo in the attachments (I do not have it in a vector file, just a jpeg)

Target Market(s)

Non tech-savvy indiduals, 30-70 years old

Industry/Entity Type

Please look at https://brushvellomart.com/development/ to see various pages and what the other designers did

Number of Pages Required

1 page

Requirements
Must have
• Verbiage on pages leave "as is" but feel free to change styles. Would like to keep existing four categories on homepage
Nice to have
• Warm and inviting homepage that evokes emotion

```html
<!DOCTYPE html>
<html lang="en">
<head>
<meta charset="UTF-8">
<title>Brushvello Mart — Photo to Canvas Art</title>
<link rel="stylesheet" href="https://fonts.googleapis.com/css2?family=Lora:wght@400;500&family=Rubik:wght@300;400;500&display=swap">
<style>
  :root {
    --ink: #111111;
    --text: #3a3a3a;
    --muted: #555555;
    --orange: #ef7d12;
    --line: #e4e4e4;
    --blue-wash: #cfe3ee;
    --yellow-wash: #fbf0c2;
    --linen: #e6ded3;
    --linen-edge: #d8cfc2;
    --wall: #d9cfc3;
    --wall-light: #ece6de;
    --floor: #c9a57a;
    --white: #ffffff;
  }
  * { box-sizing: border-box; margin: 0; padding: 0; }
  html, body { width: 1200px; height: 2543px; overflow: hidden; background: var(--white); }
  body { position: relative; font-family: "Rubik", sans-serif; color: var(--text); }
  a { color: inherit; }

  /* Brand */
  .brand { position: absolute; display: flex; align-items: center; gap: 8px; font-family: "Lora", serif; font-size: 18px; color: var(--ink); white-space: nowrap; }
  .brand-dot { width: 16px; height: 16px; border-radius: 50%; background: var(--orange); flex: none; }

  /* Header */
  .site-header { position: absolute; top: 0; left: 0; width: 1200px; height: 80px; border-bottom: 1px solid #f0f0f0; box-shadow: 0 2px 6px rgba(0,0,0,.04); }
  .site-header .brand { left: 80px; top: 28px; }
  .main-nav { position: absolute; left: 271px; top: 31px; display: flex; align-items: center; font-size: 13.5px; color: var(--ink); white-space: nowrap; }
  .main-nav a { text-decoration: none; margin-right: 34px; }
  .nav-divider { width: 1px; height: 20px; background: #ccc; margin-right: 34px; }
  .caret { display: inline-block; margin-left: 6px; border: 4px solid transparent; border-top: 5px solid var(--ink); vertical-align: -2px; }
  .cart-btn { position: absolute; left: 1083px; top: 21px; width: 37px; height: 37px; border-radius: 50%; border: 1px solid #d5d5d5; display: flex; align-items: center; justify-content: center; }

  /* Hero */
  .hero-copy { position: absolute; left: 80px; top: 172px; }
  .wash { position: absolute; border-radius: 40% 60% 55% 45% / 60% 40% 60% 40%; }
  .hero-wash { left: -40px; top: 10px; width: 350px; height: 160px; background: var(--blue-wash); opacity: .75; }
  .hero-title { position: relative; font-family: "Lora", serif; font-weight: 400; font-size: 42px; line-height: 54px; color: var(--ink); width: 340px; }
  .hero-sub { position: relative; margin-top: 36px; font-size: 16px; line-height: 25px; color: var(--muted); font-weight: 300; }
  .hero-sub strong { color: var(--orange); font-weight: 500; }
  .btn { display: inline-block; background: var(--ink); color: var(--white); font-size: 13.5px; font-weight: 500; border-radius: 20px; text-decoration: none; padding: 11px 20px; }
  .hero-copy .btn { position: relative; margin-top: 42px; }
  .hero-scene { position: absolute; left: 467px; top: 80px; width: 733px; height: 500px; border-bottom-left-radius: 120px; overflow: hidden; background: linear-gradient(180deg, var(--wall) 0%, var(--wall-light) 60%, var(--floor) 100%); }
  .frame { position: absolute; border: 4px solid var(--white); box-shadow: 0 3px 8px rgba(0,0,0,.2); }
  .frame-pet { left: 62px; top: 63px; width: 222px; height: 332px; background: linear-gradient(160deg, #a88a6e, #d9d7d3 50%, #6d5a47); }
  .frame-couple { left: 303px; top: 63px; width: 360px; height: 240px; background: linear-gradient(135deg, #3d5a2c, #8a3a2a 40%, #cfc7bb 70%, #4c6a33); }
  .furniture { position: absolute; left: 490px; top: 368px; width: 158px; height: 108px; border-radius: 16px; background: #e2c79c; }

  /* Section headings */
  .section-heading { position: absolute; left: 0; width: 1200px; text-align: center; }
  .section-heading h2 { position: relative; font-family: "Lora", serif; font-weight: 400; font-size: 32px; color: var(--ink); }
  .section-heading .wash { left: 475px; top: -10px; width: 255px; height: 66px; }

  /* Categories */
  .category { position: absolute; top: 832px; width: 260px; text-align: center; }
  .category-ring { width: 174px; height: 174px; margin: 0 auto; border-radius: 50%; display: flex; align-items: center; justify-content: center; }
  .category-photo { width: 132px; height: 132px; border-radius: 50%; }
  .category h3 { margin-top: 36px; font-size: 17px; font-weight: 500; color: var(--ink); }
  .category p { margin-top: 24px; font-size: 13.5px; line-height: 20px; font-weight: 300; color: var(--muted); }
  .category .btn { margin-top: 34px; padding: 11px 20px; }

  /* About */
  .about { position: absolute; left: 80px; top: 1327px; width: 1040px; height: 466px; background: var(--linen); border: 6px solid var(--linen-edge); box-shadow: 0 2px 6px rgba(0,0,0,.15); }
  .about .brand { left: 64px; top: 208px; font-size: 30px; gap: 12px; }
  .about .brand-dot { width: 28px; height: 28px; }
  .about-text { position: absolute; left: 427px; top: 52px; width: 550px; font-size: 13px; line-height: 20px; font-weight: 300; color: var(--ink); }
  .about-text p + p { margin-top: 20px; }

  /* Why us */
  .feature { position: absolute; top: 2040px; width: 270px; text-align: center; }
  .feature svg { display: block; margin: 0 auto; }
  .feature h3 { margin-top: 38px; font-size: 17px; font-weight: 500; color: var(--ink); }
  .feature p { margin-top: 24px; font-size: 13.5px; line-height: 20px; font-weight: 300; color: var(--muted); }

  /* Footer */
  .site-footer { position: absolute; left: 0; top: 2424px; width: 1200px; height: 119px; border-top: 1px solid var(--line); }
  .site-footer .brand { left: 80px; top: 48px; }
  .footer-links { position: absolute; left: 271px; top: 52px; display: flex; align-items: center; font-size: 11.5px; color: var(--muted); white-space: nowrap; }
  .footer-links a { margin-right: 20px; }
  .footer-links .nav-divider { margin-right: 20px; height: 18px; }
  .footer-links .copyright { margin-right: 20px; }
  .social { position: absolute; left: 992px; top: 50px; display: flex; gap: 21px; }
  .social span { width: 16px; height: 16px; border-radius: 50%; background: var(--ink); }
</style>
</head>
<body>

<header class="site-header">
  <div class="brand"><span class="brand-dot"></span>Brushvello Mart</div>
  <nav class="main-nav">
    <a href="#">Oil</a><a href="#">Watercolor</a><a href="#">Impressionist</a><a href="#">Retouching</a>
    <span class="nav-divider"></span>
    <a href="#">Testimonials</a><a href="#">FAQs</a><a href="#">Contact Us<span class="caret"></span></a>
  </nav>
  <div class="cart-btn">
    <svg width="14" height="14" viewBox="0 0 24 24" fill="none" stroke="#111" stroke-width="2" stroke-linecap="round" stroke-linejoin="round"><path d="M2 3h3l2.5 12h12l2-8H6.5"/><circle cx="9" cy="20" r="1.5"/><circle cx="18" cy="20" r="1.5"/></svg>
  </div>
</header>

<section class="hero">
  <div class="hero-copy">
    <div class="wash hero-wash"></div>
    <h1 class="hero-title">From photo to museum quality canvas art</h1>
    <p class="hero-sub">Turn your digital photos into<br><strong>one of a kind</strong> wall art</p>
    <a class="btn" href="#">Get Started</a>
  </div>
  <div class="hero-scene" role="img" aria-label="Living room wall with two framed canvas prints, a puppy portrait and a wedding couple, beside a lamp and cabinet">
    <div class="frame frame-pet"></div>
    <div class="frame frame-couple"></div>
    <div class="furniture"></div>
  </div>
</section>

<div class="section-heading" style="top:712px;">
  <div class="wash" style="background:var(--yellow-wash);"></div>
  <h2>Categories</h2>
</div>

<div class="category" style="left:60px;">
  <div class="category-ring" style="background:radial-gradient(circle, #fff 62%, #f4bcc0 100%);">
    <div class="category-photo" role="img" aria-label="Oil painting sample of a wedding couple" style="background:linear-gradient(135deg,#3f5a2e,#8c4a35 50%,#d8cfc3);"></div>
  </div>
  <h3>Oil</h3>
  <p>Lorem ipsum dolor sitamet<br>consectetur adipiscing elit</p>
  <a class="btn" href="#">Try Now</a>
</div>

<div class="category" style="left:333px;">
  <div class="category-ring" style="background:radial-gradient(circle, #fff 62%, #bcd3e6 100%);">
    <div class="category-photo" role="img" aria-label="Watercolor sample of a mother with her baby" style="background:linear-gradient(135deg,#f4e3da,#e9c4b4 50%,#fbf3ef);"></div>
  </div>
  <h3>Watercolor</h3>
  <p>Lorem ipsum dolor sitamet<br>consectetur adipiscing elit</p>
  <a class="btn" href="#">Try Now</a>
</div>

<div class="category" style="left:606px;">
  <div class="category-ring" style="background:radial-gradient(circle, #fff 62%, #b9e1ec 100%);">
    <div class="category-photo" role="img" aria-label="Impressionist sample of a traveler at a canal" style="background:linear-gradient(180deg,#6fa8d6,#b8553d 50%,#2fa9a0);"></div>
  </div>
  <h3>Impressionist</h3>
  <p>Lorem ipsum dolor sitamet<br>consectetur adipiscing elit</p>
  <a class="btn" href="#">Try Now</a>
</div>

<div class="category" style="left:880px;">
  <div class="category-ring" style="background:radial-gradient(circle, #fff 62%, #f6cbb1 100%);">
    <div class="category-photo" role="img" aria-label="Retouched photo sample of two children with ice cream" style="background:linear-gradient(135deg,#c9b7a6,#e7c3a6 50%,#5a7d96);"></div>
  </div>
  <h3>Digital Photo / Retouching</h3>
  <p>Lorem ipsum dolor sitamet<br>consectetur adipiscing elit</p>
  <a class="btn" href="#">Try Now</a>
</div>

<section class="about">
  <div class="brand"><span class="brand-dot"></span>Brushvello Mart</div>
  <div class="about-text">
    <p>At Brushvello Mart, we take your digital photo and turn it into a one-of-a-kind piece of artwork!</p>
    <p>The process couldn’t be any easier. Simply upload your photo, choose your art style and size, and let our team of skilled digital artists do the rest. Do you want to put your digital photo on canvas without an art style? No problem! Just choose the “Digital Photo/ Retouching” category and upload your photo. We can print your photo “as is” or do some minor retouching (e.g. remove objects, enhance colors, lighten photo, etc)</p>
    <p>You will receive a proof in your email to approve within 1-2 days. Once approved, your customized artwork will be transferred to canvas and shipped from our design studio in Florida.</p>
    <p>Brushvello Mart art makes a great gift for just about any special occasion. Know someone with an upcoming birthday, anniversary, housewarming party, wedding or other event? We’ve got you covered!</p>
    <p>Turn your cherished memories into a customized canvas masterpiece today!</p>
  </div>
</section>

<div class="section-heading" style="top:1925px;">
  <div class="wash" style="background:var(--blue-wash);"></div>
  <h2>Why Us?</h2>
</div>

<div class="feature" style="left:132px;">
  <svg width="70" height="70" viewBox="0 0 70 70" fill="none" stroke-width="2" stroke-linecap="round" stroke-linejoin="round">
    <g stroke="#2e8b3a"><circle cx="35" cy="20" r="9"/><path d="M31 29v5h8v-5"/><path d="M35 4v3M21 8l2 2M49 8l-2 2M17 20h3M50 20h3"/></g>
    <g stroke="#111"><path d="M6 56l10-10c3-3 7-4 11-2l8 3h9c2 0 3 2 1 4l-10 3"/><path d="M30 52l16-6c4-2 8-3 10 0l-20 14H18l-6 4"/><path d="M4 54l8 10"/></g>
  </svg>
  <h3>Your Idea Your Design</h3>
  <p>Each art piece is customized for you! You choose your size, orientation and art style. Makes a perfect gift!!!</p>
</div>

<div class="feature" style="left:465px;">
  <svg width="70" height="70" viewBox="0 0 70 70" fill="none" stroke-width="2" stroke-linecap="round" stroke-linejoin="round">
    <g stroke="#2a9fc9"><circle cx="20" cy="20" r="12"/><path d="M20 13v7l5 3"/></g>
    <g stroke="#111"><path d="M32 22h14l12 14v14h-6"/><path d="M46 22v14h12"/><path d="M10 38v12h6"/><path d="M28 50h16"/><circle cx="22" cy="50" r="5"/><circle cx="48" cy="50" r="5"/></g>
  </svg>
  <h3>Fast Shipping</h3>
  <p>Your artwork is printed and shipped in the USA! We offer fast turnaround with transit times typically 3-7 days. Free tracking with each order!!</p>
</div>

<div class="feature" style="left:798px;">
  <svg width="70" height="70" viewBox="0 0 70 70" fill="none" stroke-width="2" stroke-linecap="round" stroke-linejoin="round">
    <g stroke="#d8332f"><circle cx="35" cy="30" r="20"/><path d="M35 20l3 7 7 .5-5.5 4.5 2 7-6.5-4-6.5 4 2-7L25 27.5l7-.5z"/></g>
    <g stroke="#111"><path d="M15 42h40v14H15z"/><path d="M15 46l-8 4 4 4-4 4h8M55 46l8 4-4 4 4 4h-8"/></g>
  </svg>
  <h3>High Quality</h3>
  <p>We’ve put a lot of effort ensuring your artwork is of the highest quality. Each piece is printed on the highest quality, gallery grade canvas. It is ready to hang upon arrival.!</p>
</div>

<footer class="site-footer">
  <div class="brand"><span class="brand-dot"></span>Brushvello Mart</div>
  <div class="footer-links">
    <span class="copyright">© 2023 Brushvello Mart</span>
    <span class="nav-divider"></span>
    <a href="#">Testimonials</a><a href="#">FAQs</a><a href="#">Contact Us</a>
    <span class="nav-divider"></span>
    <a href="#">info@brushvellomart.com</a>
  </div>
  <div class="social"><span></span><span></span><span></span><span></span></div>
</footer>

</body>
</html>
```